New design for a hotel booking website

I am looking to re-design my hotel booking website pinecrestlodgings.net. Please find the specs attached. Delivery in PSD format. Two pages total: (i) homepage and (ii) inner page.
I want the design to be very simple to navigate and have a feel that is related to Banff, Canada. You can keep a similar layout as the current website.
Requirements
1) Homepage
- Booking form above the fold containing the check in & check out dates, # of rooms and the Search button
- Quality image relating to the city of Banff to make it clear what city this is (no slider - I don't want any animation)
- A section for featured hotels (3-5 items)
- A section for links to other sections on the website (currently under "Explore Banff")
- A section for articles and local guides
- A weather widget (either in the header or somewhere else, similar to this one http://clipvuebox.com/t/QX7RKLd4P2)
2) Hotel listings page - http://www.pinecrestlodgings.net/hotels
- Left or right sidebar – must contain the booking form with the same fields as on the homepage
- A section of why to book hotels with us under the booking form
- Each hotel listing should contain the following
Hotel name
Star rating
Short description (same as currently on the website)
Thumbnail
Address
A button to Check Rates
Notes
- I want the design to be user friendly, simple and easy to use
- I want it to be related to Banff. Banff is a resort town in Alberta, Canada with mountains for skiing in the winter and parks and wildlife nature in the summer.
- Delivery format: PSD
- I want the layout to be easily convertible into a responsive design
- Small social media icon to the Chatterly page (with the option to add Vidloom and Quibbit in the future)
Some competing website examples:
1) ridgemoorvale.com/Places-to-Stay/Hotels-Inns
2) torvikinns.org
Some examples of websites I liked:
1) http://www.glendrova.com/accommodation/hotels/
2) http://www.lodgetrailmarvenby.com/
Anyone looking to book their stay in Banff, AB, Canada.
Travel
2 page

```html
<!DOCTYPE html>
<html lang="en">
<head>
<meta charset="utf-8">
<title>Pinecrest Lodgings – Compare Prices on Accommodations in Banff</title>
<link href="https://fonts.googleapis.com/css2?family=Lato:wght@300;400;700&display=swap" rel="stylesheet">
<style>
:root{
  --teal:#1f6f8b;
  --green:#2b6e46;
  --green-dark:#1d6a37;
  --text:#3a3a3a;
  --line:#dcdcdc;
  --panel:#f2f2f2;
  --band:#e4e4e4;
}
*{box-sizing:border-box;margin:0;padding:0}
html,body{width:796px;height:1200px;overflow:hidden;background:#fff}
body{font-family:'Lato',sans-serif;color:var(--text);font-size:9px;position:relative}
a{color:inherit;text-decoration:none}
.abs{position:absolute}

/* header */
.brand{left:82px;top:9px}
.brand-name{font-size:20px;font-weight:400;color:var(--teal);line-height:22px}
.brand-tag{font-size:10px;font-weight:400;color:var(--teal);margin-top:1px}
.call{right:85px;top:12px;color:var(--green);font-size:13px;font-weight:300}
.call b{font-size:19px;font-weight:300;color:var(--teal)}

/* nav */
.nav{left:0;top:45px;width:796px;height:32px;background:var(--band)}
.nav ul{list-style:none;display:flex;position:absolute;left:82px;top:0;height:32px}
.nav li{font-size:9.5px;font-weight:300;color:#555;padding:0 13px;line-height:32px;text-transform:uppercase}
.nav li.active{background:var(--green-dark);color:#fff;font-weight:700}
.social{position:absolute;right:84px;top:6px;display:flex;gap:3px}
.social span{font-size:7px;color:#333;background:#ececec;padding:0 4px;line-height:20px;height:20px}

/* hero */
.hero{left:0;top:77px;width:796px;height:255px;background:linear-gradient(180deg,#5d6a58 0%,#8a7c64 45%,#6c4a3a 75%,#4a4642 100%)}
.hero-right{left:713px;top:77px;width:83px;height:255px;background:linear-gradient(180deg,#7a3a28,#3a2a24)}
.search{left:515px;top:77px;width:198px;height:255px;background:rgba(236,242,244,.93);padding:14px 19px}
.search h2{font-size:18px;font-weight:300;color:var(--teal);text-align:center;margin-bottom:14px}
.field{height:24px;background:#fff;border:1px solid #ccc;font-size:7px;color:#555;padding:0 6px;line-height:22px;position:relative}
.field::after{content:"";position:absolute;right:6px;top:9px;border:3px solid transparent;border-top:4px solid #999}
.label{font-size:8.5px;color:var(--teal);margin:12px 0 3px}
.row{display:flex;gap:8px}
.row .col{flex:1}
.btn-search{margin-top:18px;height:28px;background:var(--green-dark);color:#fff;font-size:13px;text-align:center;line-height:28px;font-weight:300}

/* guides bar */
.guides{left:27px;top:332px;width:769px;height:24px;background:#f4f4f4;padding-left:55px;line-height:24px;font-size:8.5px;font-weight:300}
.guides b{font-weight:700;color:#222}
.guides .more{color:var(--teal);font-weight:400;font-size:7.5px}
.guides svg{position:absolute;left:55px;top:6px}
.guides .txt{margin-left:17px}

/* welcome */
.weather{left:91px;top:381px;width:192px;height:109px;background:linear-gradient(135deg,#4bb0c6,#2f8ea6);color:#fff}
.weather .cond{position:absolute;left:7px;bottom:9px;font-size:21px;font-weight:300;letter-spacing:-.3px}
.vsep{left:307px;top:377px;width:1px;height:120px;background:var(--line)}
.welcome{left:333px;top:378px;width:362px}
.welcome h1{font-size:16.5px;font-weight:300;color:var(--green);margin-bottom:8px}
.welcome p{font-size:8.8px;line-height:14px;font-weight:300;color:#444}
.welcome .read{display:block;margin-top:7px;font-size:10.5px;color:var(--green);font-weight:300}
.hr{left:82px;width:631px;height:1px;background:var(--line)}

/* featured */
.card{top:537px;width:199px;height:164px;background:var(--panel);padding:4px 5px}
.card .photo{height:92px}
.card h3{font-size:10px;font-weight:300;color:var(--green);margin:6px 1px 3px}
.card p{font-size:8px;line-height:11.5px;font-weight:300;color:#444;padding:0 1px}
.card .more{display:block;margin:7px 1px 0;font-size:8px;color:#555;font-weight:300}

/* articles */
.sec-title{font-size:14px;font-weight:300;color:var(--green)}
.articles{left:82px;top:750px;width:410px}
.articles .sec-title{padding-bottom:11px;border-bottom:1px solid var(--line)}
.article{display:flex;gap:9px;padding:17px 0 17px;border-bottom:1px solid var(--line)}
.article:last-of-type{border-bottom:none}
.article .thumb{width:105px;height:73px;flex:none;background:linear-gradient(180deg,#b7c2c6 0%,#7a8680 45%,#5e5a52 100%)}
.article h4{font-size:10px;font-weight:300;color:var(--teal);margin:-2px 0 4px}
.article p{font-size:8px;line-height:12px;font-weight:300;color:#444}
.viewall{display:inline-block;border:1px solid #ccc;font-size:8.5px;padding:0 11px;line-height:20px;color:#444;font-weight:300}
.colsep{left:507px;top:750px;width:1px;height:266px;background:var(--line)}
.explore{left:525px;top:750px;width:188px}
.explore .sec-title{padding-bottom:11px;border-bottom:1px solid var(--line)}
.explore ul{list-style:none}
.explore li{display:flex;justify-content:space-between;align-items:center;height:29.5px;border-bottom:1px solid var(--line);padding:0 10px;font-size:8.5px;font-weight:300;color:#333}
.explore li:last-child{border-bottom:none}

/* info boxes */
.info{left:82px;top:1040px;width:631px;height:130px;border:1px solid var(--line);display:flex}
.info .box{padding:15px 13px 0}
.info .box+.box{border-left:1px solid var(--line)}
.info h5{font-size:13.5px;font-weight:300;color:#333;margin-bottom:8px}
.info p{font-size:8px;line-height:11.5px;font-weight:300;color:#444}
.quote{font-style:italic;color:#888 !important;line-height:14px !important}
.quote .mark{font-size:22px;color:#ccc;font-style:normal;vertical-align:-6px;line-height:0}
.client{display:block;margin-top:8px;font-size:10px;color:var(--teal);font-weight:300}
.fb{display:flex;gap:8px}
.fb .sq{width:29px;height:29px;background:var(--teal);flex:none}

/* footer */
.footer{left:84px;top:1180px;width:629px;display:flex;justify-content:space-between;font-size:7.5px;font-weight:300;color:#444}
</style>
</head>
<body>

<header>
  <div class="abs brand">
    <div class="brand-name">Pinecrest Lodgings</div>
    <div class="brand-tag">Compare prices on accommodations in Banff</div>
  </div>
  <div class="abs call">Call Now: <b>800 555 0142</b></div>
</header>

<nav class="abs nav">
  <ul>
    <li class="active">Home</li>
    <li>Banff Hotels</li>
    <li>Banff Resorts</li>
    <li>Lodges</li>
    <li>Inns &amp; Motels</li>
    <li>Contact Us</li>
  </ul>
  <div class="social"><span>Chatterly</span><span>Quibbit</span></div>
</nav>

<section>
  <div class="abs hero" role="img" aria-label="Photo of Banff Avenue with shops, cars and mountains behind"></div>
  <div class="abs hero-right" role="img" aria-label="Continuation of the street photo with a wooden town sign"></div>
  <form class="abs search">
    <h2>SEARCH BANFF</h2>
    <div class="field">Select Accomodation Type</div>
    <div class="row">
      <div class="col"><div class="label">From</div><div class="field">Select Date</div></div>
      <div class="col"><div class="label">To</div><div class="field">Select Date</div></div>
    </div>
    <div class="label">Number of Rooms</div>
    <div class="field">1</div>
    <div class="btn-search">SEARCH</div>
  </form>
</section>

<div class="abs guides">
  <svg width="14" height="13" viewBox="0 0 14 13"><rect x="1" y="2" width="9" height="10" fill="none" stroke="#2a8fb0" stroke-width="1.3"/><path d="M5 9 L12 2" stroke="#2a8fb0" stroke-width="1.5"/></svg>
  <span class="txt"><b>BANFF Guides:</b> Lorem Ipsum is simply dummy text of the printing and typesetting industry. <a class="more">+ Read More</a></span>
</div>

<section>
  <div class="abs weather">
    <svg class="abs" style="left:12px;top:13px" width="60" height="55" viewBox="0 0 60 55"><path d="M30 4 A22 22 0 1 0 50 38 A18 18 0 0 1 30 4Z" fill="#fff"/><path d="M18 48 h30 a8 8 0 0 0 0-16 a10 10 0 0 0-19-2 a8 8 0 0 0-11 18z" fill="#fff" stroke="#3ba0b9" stroke-width="2"/></svg>
    <div class="cond">Partly Cloudy, 5ºc</div>
  </div>
  <div class="abs vsep"></div>
  <div class="abs welcome">
    <h1>WELCOME TO PINECREST LODGINGS</h1>
    <p>Lorem ipsum dolor sit amet, consectetur adipiscing elit. Nulla convallis egestas rhoncus. Donec facilisis fermentum sem, ac viverra ante luctus vel. Donec vel mauris quam. Lorem ipsum dolor sit amet, consectetur adipiscing elit. Nulla convallis egestas rhoncus. Donec vel mauris quam. Lorem ipsum dolor sit amet, consectetur adipiscing elit. Nulla convallis egestas rhoncus.</p>
    <a class="read">READ MORE</a>
  </div>
</section>

<div class="abs hr" style="top:515px"></div>

<section>
  <article class="abs card" style="left:82px">
    <div class="photo" role="img" aria-label="Photo of a large lodge in snow with mountains behind" style="background:linear-gradient(180deg,#9fb0c4,#8a6f57 60%,#d9d6d2)"></div>
    <h3>The Stonecrest Lodge</h3>
    <p>Lorem Ipsum is simply dummy text of the print-ing and typesetting industry.</p>
    <a class="more">+ Read More</a>
  </article>
  <article class="abs card" style="left:298px">
    <div class="photo" role="img" aria-label="Photo of a lodge at dusk among tall pine trees" style="background:linear-gradient(180deg,#6f9ed0,#2f3f34 55%,#3b4a3e)"></div>
    <h3>Elkhorn Royal Alpine Lodge</h3>
    <p>Lorem Ipsum is simply dummy text of the print-ing and typesetting industry.</p>
    <a class="more">+ Read More</a>
  </article>
  <article class="abs card" style="left:515px">
    <div class="photo" role="img" aria-label="Photo of a lodge entrance with flags and mountains" style="background:linear-gradient(180deg,#8fb1d6,#7d8a7a 45%,#6b5a48 75%,#8c8a84)"></div>
    <h3>Bowridge Park Lodges</h3>
    <p>Lorem Ipsum is simply dummy text of the print-ing and typesetting industry.</p>
    <a class="more">+ Read More</a>
  </article>
</section>

<div class="abs hr" style="top:724px"></div>

<section class="abs articles">
  <h2 class="sec-title">Articles &amp; Local Guides</h2>
  <article class="article">
    <div class="thumb" role="img" aria-label="Photo of Banff street with mountain behind"></div>
    <div>
      <h4>BANFF A PLACE TO VISIT</h4>
      <p>Lorem Ipsum is simply dummy text of the printing and typesetting industry. Lorem Ipsum has been the industry's standard dummy text ever since the 1500s, when an unknown printer took a galley of type and scrambled it to make a type specimen book. It has survived not only five centuries, but also the leap into electronic typesetting, remaining essentially unchanged.</p>
    </div>
  </article>
  <article class="article">
    <div class="thumb" role="img" aria-label="Photo of Banff street with mountain behind"></div>
    <div>
      <h4>BANFF A PLACE TO VISIT</h4>
      <p>Lorem Ipsum is simply dummy text of the printing and typesetting industry. Lorem Ipsum has been the industry's standard dummy text ever since the 1500s, when an unknown printer took a galley of type and scrambled it to make a type specimen book. It has survived not only five centuries, but also the leap into electronic typesetting, remaining essentially unchanged.</p>
    </div>
  </article>
  <a class="viewall">View All</a>
</section>

<div class="abs colsep"></div>

<aside class="abs explore">
  <h2 class="sec-title">Explore Banff</h2>
  <ul>
    <li>Things to do in Banff <svg width="7" height="6" viewBox="0 0 7 6"><path d="M0 3h6M4 1l2 2-2 2" stroke="#1f6f8b" fill="none"/></svg></li>
    <li>Banff Festivals <svg width="7" height="6" viewBox="0 0 7 6"><path d="M0 3h6M4 1l2 2-2 2" stroke="#1f6f8b" fill="none"/></svg></li>
    <li>Experience Summit Gondola <svg width="7" height="6" viewBox="0 0 7 6"><path d="M0 3h6M4 1l2 2-2 2" stroke="#1f6f8b" fill="none"/></svg></li>
    <li>Heli Sightseeing in Banff <svg width="7" height="6" viewBox="0 0 7 6"><path d="M0 3h6M4 1l2 2-2 2" stroke="#1f6f8b" fill="none"/></svg></li>
    <li>Hiking in Banff <svg width="7" height="6" viewBox="0 0 7 6"><path d="M0 3h6M4 1l2 2-2 2" stroke="#1f6f8b" fill="none"/></svg></li>
    <li>Camping &amp; Campgrounds <svg width="7" height="6" viewBox="0 0 7 6"><path d="M0 3h6M4 1l2 2-2 2" stroke="#1f6f8b" fill="none"/></svg></li>
    <li>Hotels near Upper Hot Springs <svg width="7" height="6" viewBox="0 0 7 6"><path d="M0 3h6M4 1l2 2-2 2" stroke="#1f6f8b" fill="none"/></svg></li>
    <li>Nearby Cities <svg width="7" height="6" viewBox="0 0 7 6"><path d="M0 3h6M4 1l2 2-2 2" stroke="#1f6f8b" fill="none"/></svg></li>
  </ul>
</aside>

<section class="abs info">
  <div class="box" style="width:217px">
    <h5>Client’s Testimonials:</h5>
    <p class="quote"><span class="mark">“</span> Lorem ipsum dolor sit amet, consectetur adipiscing elit. Nulla convallis egestas rhoncus. Donec facilisis fermentum sem, ac viverra ante luctus vel. Donec vel mauris quam.</p>
    <a class="client">Happy Client</a>
  </div>
  <div class="box" style="width:226px">
    <h5>Hotel Customer Service</h5>
    <p>If you have already booked a hotel reservation and need assistance, you can contact our Customer Service at 800-555-0199. If you call this 800 number please have your trip number, phone number and email that you entered while making your reservation available.</p>
  </div>
  <div class="box" style="flex:1">
    <h5>Social Connect</h5>
    <div class="fb"><div class="sq"></div><p>Like us on Chatterly for a chance to win a free 2-night stay in Banff!</p></div>
  </div>
</section>

<footer class="abs footer">
  <span>© 2015 Pinecrest Lodgings. All rights reserved.</span>
  <span>Contacts | FAQ | Terms &amp; Conditions | Privacy Policy</span>
</footer>

</body>
</html>
```